" Soluçoes de tecnologia focadas em impressao e outsourcing de impressao visando a reduçao de custos de impressao e a melhoria de processos para pequenas, médias e grandes empresas corporativas e governo através de licitações. Atendimento ao público(balcão) com soluções de grafica rápida, impressão de dados variáveis, impressão de provas de consursos Gerenciar e racionalizar os processos de impressao/cópia através de uso inteligente de tecnologia de última geraçao. Contabilizar páginas/cópias impressas, gerenciar suprimentos. Otimizar processos internos para cada departamento e necessidade. Solução de digitalização de documentos. "

```html
<!DOCTYPE html>
<html lang="pt-BR">
<head>
<meta charset="utf-8">
<title>Tinta Nova — Cartão de visita</title>
<link href="https://fonts.googleapis.com/css2?family=Montserrat:wght@400;500;700;800&display=swap" rel="stylesheet">
<style>
  :root{
    --bg:#e9eaec;
    --card-dark:#0d0d0d;
    --card-light:#ffffff;
    --ink:#2a2a2a;
    --ink-soft:#555a60;
    --brand-blue:#1f8ed6;
    --white:#ffffff;
  }
  *{box-sizing:border-box;margin:0;padding:0}
  html,body{width:1200px;height:1200px;overflow:hidden}
  body{background:var(--bg);font-family:"Montserrat",sans-serif;position:relative}
  .card{
    position:absolute;left:170px;width:860px;height:491px;border-radius:30px;overflow:hidden;
    box-shadow:0 10px 30px rgba(0,0,0,.12);
  }
  /* front */
  .card--front{top:70px;background:var(--card-dark);color:var(--white)}
  .front-brand{position:absolute;top:170px;left:0;right:0;text-align:center}
  .front-brand .dot{
    display:block;width:72px;height:72px;border-radius:50%;background:var(--brand-blue);margin:0 auto 22px;
  }
  .front-brand .name{font-weight:800;font-size:64px;letter-spacing:2px;line-height:1;color:var(--white)}
  .front-url{
    position:absolute;bottom:72px;left:0;right:0;text-align:center;
    font-weight:500;font-size:22px;letter-spacing:6px;color:var(--white)
  }
  /* back */
  .card--back{top:631px;background:var(--card-light);color:var(--ink)}
  .back-head{position:absolute;top:78px;left:80px;display:flex;align-items:center}
  .back-brand{display:flex;align-items:center;gap:12px;padding-right:26px;border-right:2px solid var(--ink);height:78px}
  .back-brand .dot{width:26px;height:26px;border-radius:50%;background:var(--brand-blue)}
  .back-brand .name{font-weight:800;font-size:30px;color:var(--ink);letter-spacing:.5px}
  .person{padding-left:24px}
  .person .full-name{font-weight:500;font-size:30px;line-height:1.15}
  .person .role{font-weight:400;font-size:19px;color:var(--ink-soft);margin-top:4px}
  .contacts{position:absolute;left:95px;top:250px;list-style:none}
  .contacts li{display:flex;align-items:center;gap:12px;font-size:21px;color:var(--ink-soft);line-height:1;margin-bottom:14px}
  .contacts svg{width:18px;height:18px;fill:var(--ink-soft);flex:none}
  .social{position:absolute;right:120px;bottom:52px;display:flex;align-items:center;gap:10px;font-size:21px;color:var(--brand-blue)}
  .social .square{width:20px;height:20px;background:var(--brand-blue);border-radius:3px}
</style>
</head>
<body>
  <section class="card card--front">
    <div class="front-brand">
      <span class="dot"></span>
      <span class="name">TINTA NOVA</span>
    </div>
    <p class="front-url">www.tintanova.com.br</p>
  </section>

  <section class="card card--back">
    <header class="back-head">
      <div class="back-brand">
        <span class="dot"></span>
        <span class="name">TINTA NOVA</span>
      </div>
      <div class="person">
        <p class="full-name">Nome Sobrenome</p>
        <p class="role">Cargo</p>
      </div>
    </header>
    <ul class="contacts">
      <li><svg viewBox="0 0 24 24" aria-hidden="true"><path d="M12 2a7 7 0 0 0-7 7c0 5 7 13 7 13s7-8 7-13a7 7 0 0 0-7-7zm0 9.5A2.5 2.5 0 1 1 12 6.5a2.5 2.5 0 0 1 0 5z"/></svg>Nome da Rua, 00 - Centro</li>
      <li><svg viewBox="0 0 24 24" aria-hidden="true"><path d="M6.6 10.8a15 15 0 0 0 6.6 6.6l2.2-2.2a1 1 0 0 1 1-.25 11.4 11.4 0 0 0 3.6.57 1 1 0 0 1 1 1V20a1 1 0 0 1-1 1A17 17 0 0 1 3 4a1 1 0 0 1 1-1h3.5a1 1 0 0 1 1 1c0 1.25.2 2.45.57 3.570a1 1 0 0 1-.25 1z"/></svg>91 0000-0000</li>
      <li><svg viewBox="0 0 24 24" aria-hidden="true"><path d="M3 5h18v14H3zm2 2v.5l7 4.5 7-4.5V7z"/></svg>contato@tintanova.com.br</li>
    </ul>
    <div class="social"><span class="square"></span>/tintanova</div>
  </section>
</body>
</html>
```